Design for a Note buying company that attracts landlords and seller financed notes

I need a card designed. I want a simple clean front with my logo and contact info. On the back I want some big and bold words to get a message across.

Our Company buys Notes (mortgages) and we want to convey the sense of financial security. Our number one market that we pursue is tired landlords.

If you want to understand our business you can visit our website. www.lakeviewpaperfund.com

Do not use any Clip Art in the design, it will not be accepted. I want a custom designed card not something I could throw together myself. Simple clean and drive the message home.

Target Market(s)

Landlords, seller financed note holders

Industry/Entity Type

Mortgage

Contact Information for Business Card

Simple clean and bold. I need to grab the attention of the customer. It should convey a professional touch.

Font styles to use
Sans Serif

Colors
ec2229
ffffff

Requirements
Must have
• Clean front with logo and contact information
Front colors should match logo

Back should be bold and grab attention. Back colors are open to ideas
Nice to have
• The Back May use the phrase "No more Tentants, No more Toilets" "More Time, More Cash"

I'm open to other ideas about grabbing a landlords attention

I'm open to a square card design
I like cards with round corners as well
Should not have
• any clip art! must be custom designs.

```html
<!DOCTYPE html>
<html lang="en">
<head>
<meta charset="utf-8">
<title>Lakeview Paper Fund – Business Card</title>
<link href="https://fonts.googleapis.com/css2?family=Oswald:wght@500&family=Poppins:wght@400;600;800&display=swap" rel="stylesheet">
<style>
  :root {
    --stage: #5f5f60;
    --card: #272728;
    --card-edge: #1e1e1f;
    --red: #ec2229;
    --white: #ffffff;
    --soft: #d9d9d9;
    --rule: #bdbdbd;
  }
  * { box-sizing: border-box; margin: 0; padding: 0; }
  html, body { width: 1200px; height: 800px; overflow: hidden; }
  body {
    background: var(--stage);
    font-family: "Poppins", sans-serif;
    display: flex;
    align-items: center;
    justify-content: center;
    gap: 40px;
  }
  .card {
    position: relative;
    width: 540px;
    height: 310px;
    background: var(--card);
    border-radius: 24px;
    overflow: hidden;
    box-shadow: 0 14px 30px rgba(0,0,0,0.35);
  }

  /* Contact side */
  .identity {
    position: absolute;
    left: 40px;
    top: 92px;
    width: 170px;
    text-align: right;
  }
  .identity__name {
    font-family: "Oswald", sans-serif;
    font-weight: 500;
    font-size: 30px;
    line-height: 1;
    color: var(--red);
    letter-spacing: 0.5px;
  }
  .identity__role {
    font-size: 15px;
    color: var(--white);
    margin-top: 4px;
  }
  .divider {
    position: absolute;
    left: 232px;
    top: 58px;
    width: 1px;
    height: 120px;
    background: var(--rule);
  }
  .contact {
    position: absolute;
    left: 254px;
    top: 52px;
    color: var(--white);
    font-size: 13px;
    line-height: 1.35;
  }
  .contact__address { margin-bottom: 8px; }
  .contact__list { list-style: none; }
  .contact__item {
    display: flex;
    align-items: center;
    gap: 8px;
    line-height: 1.4;
  }
  .contact__icon { width: 11px; height: 11px; flex: none; }

  .message-band {
    position: absolute;
    left: 0;
    right: 0;
    bottom: 18px;
    height: 34px;
    background: var(--red);
    color: var(--white);
    font-weight: 800;
    font-size: 11.5px;
    letter-spacing: -0.2px;
    display: flex;
    align-items: center;
    justify-content: center;
    word-spacing: 1px;
  }

  /* Brand side */
  .card--brand { border-bottom: 3px solid var(--red); }
  .brand {
    position: absolute;
    inset: 0;
    display: flex;
    align-items: center;
    justify-content: center;
    gap: 14px;
  }
  .brand__mark {
    width: 26px;
    height: 26px;
    background: var(--red);
  }
  .brand__name {
    font-weight: 600;
    font-size: 34px;
    color: var(--soft);
    letter-spacing: 1px;
    text-transform: uppercase;
  }
</style>
</head>
<body>

  <section class="card card--contact">
    <div class="identity">
      <p class="identity__name">DANIEL REYES</p>
      <p class="identity__role">President</p>
    </div>

    <div class="divider"></div>

    <div class="contact">
      <p class="contact__address">412 Birchwood Court<br>Cedar Falls, Alaska 34581</p>
      <ul class="contact__list">
        <li class="contact__item">
          <svg class="contact__icon" viewBox="0 0 12 12"><path d="M2.5 1 L4.5 1 L5 3.5 L3.8 4.4 Q5 7 7.6 8.2 L8.5 7 L11 7.5 L11 9.5 Q10 11 8.5 11 Q1 9 1 2.5 Q1 1.5 2.5 1Z" fill="var(--red)"/></svg>
          369-555-0142
        </li>
        <li class="contact__item">
          <svg class="contact__icon" viewBox="0 0 12 12"><rect x="3" y="0.8" width="6" height="10.4" rx="1" fill="none" stroke="var(--white)" stroke-width="1.2"/></svg>
          369-555-0178
        </li>
        <li class="contact__item">
          <svg class="contact__icon" viewBox="0 0 12 12"><rect x="0.5" y="2" width="11" height="8" fill="var(--red)"/><path d="M0.5 2 L6 6.5 L11.5 2" fill="none" stroke="var(--card)" stroke-width="1"/></svg>
          info@lakeviewpaperfund.com
        </li>
        <li class="contact__item">
          <svg class="contact__icon" viewBox="0 0 12 12"><circle cx="6" cy="6" r="5.5" fill="var(--red)"/><path d="M0.5 6 H11.5 M6 0.5 Q3 6 6 11.5 M6 0.5 Q9 6 6 11.5" fill="none" stroke="var(--card)" stroke-width="0.8"/></svg>
          www.lakeviewpaperfund.com
        </li>
      </ul>
    </div>

    <p class="message-band">NO MORE TENTANTS &nbsp;|&nbsp; NO MORE TOILETS &nbsp;|&nbsp; MORE TIME &nbsp;|&nbsp; MORE CASH</p>
  </section>

  <section class="card card--brand">
    <div class="brand">
      <span class="brand__mark"></span>
      <span class="brand__name">Lakeview Paper Fund</span>
    </div>
  </section>

</body>
</html>
```